Important Solar Energy Company Needs a Stationery Design

I need a modern, attractive, corporate stationary design (letter head and business card)
Attached Company Logo

Target Market(s)

Upmarket

Industry/Entity Type

Business

Colors
ec1f27
ffffff
757575
cbcbcb
000000

```html
<!DOCTYPE html>
<html lang="en">
<head>
<meta charset="utf-8">
<title>Solvanta Business Card</title>
<link href="https://fonts.googleapis.com/css2?family=Montserrat:wght@400;500;600&display=swap" rel="stylesheet">
<style>
  :root {
    --brand-red: #ec1f27;
    --paper: #ffffff;
    --ink: #1a1a1a;
    --mid-grey: #757575;
    --light-grey: #cbcbcb;
    --backdrop: #e4e4e6;
  }
  * { box-sizing: border-box; margin: 0; padding: 0; }
  html, body {
    width: 1200px; height: 900px; overflow: hidden;
    background: var(--backdrop);
    font-family: "Montserrat", sans-serif;
  }
  .canvas {
    width: 1200px; height: 900px;
    display: flex; flex-direction: column; align-items: center; justify-content: center;
    gap: 56px;
  }
  .card {
    width: 560px; height: 320px; position: relative; overflow: hidden;
    box-shadow: 0 2px 6px rgba(0,0,0,0.12);
  }
  /* back */
  .card-back { background: var(--brand-red); color: var(--paper); }
  .back-mark {
    position: absolute; left: 50%; top: 118px; transform: translate(-50%, -50%);
    display: flex; align-items: center; gap: 16px;
  }
  .back-mark .dot { width: 44px; height: 44px; border-radius: 50%; background: var(--paper); }
  .back-mark .name { font-size: 38px; font-weight: 500; letter-spacing: 2px; }
  .back-web {
    position: absolute; left: 0; right: 0; bottom: 56px; text-align: center;
    font-size: 15px; font-weight: 500; letter-spacing: 3px;
  }
  /* front */
  .card-front { background: var(--paper); }
  .front-logo {
    position: absolute; right: 40px; top: 40px;
    display: flex; align-items: center; gap: 12px;
  }
  .front-logo .dot { width: 34px; height: 34px; border-radius: 50%; background: var(--brand-red); }
  .front-logo .name { font-size: 24px; font-weight: 500; letter-spacing: 2px; color: var(--ink); }
  .contact {
    position: absolute; left: 292px; top: 118px;
    font-size: 14px; line-height: 1.45; color: var(--mid-grey);
  }
  .contact .address { margin-bottom: 12px; }
  .contact-row { display: flex; align-items: center; gap: 8px; }
  .contact-row svg { width: 14px; height: 14px; flex: none; }
  .person { position: absolute; left: 40px; bottom: 56px; }
  .person .full-name { font-size: 20px; font-weight: 600; color: var(--brand-red); letter-spacing: 0.5px; }
  .person .role { font-size: 13px; color: var(--mid-grey); letter-spacing: 0.5px; margin-top: 2px; }
  .accent-bar {
    position: absolute; left: 292px; right: 0; bottom: 0; height: 14px;
    background: var(--brand-red);
  }
</style>
</head>
<body>
<main class="canvas">
  <section class="card card-back" aria-label="Business card back">
    <div class="back-mark"><span class="dot"></span><span class="name">SOLVANTA</span></div>
    <div class="back-web">www.solvanta.com</div>
  </section>

  <section class="card card-front" aria-label="Business card front">
    <div class="front-logo"><span class="dot"></span><span class="name">SOLVANTA</span></div>
    <div class="contact">
      <p class="address">27 Harbor Row<br>Riverton, OH 44012</p>
      <p class="contact-row">
        <svg viewBox="0 0 14 14"><circle cx="7" cy="7" r="7" fill="#ec1f27"/><rect x="4.8" y="3" width="4.4" height="8" rx="0.8" fill="none" stroke="#fff" stroke-width="1.1"/></svg>
        05550 111 222
      </p>
      <p class="contact-row">
        <svg viewBox="0 0 14 14"><circle cx="7" cy="7" r="7" fill="#ec1f27"/><path d="M4 6 Q7 3 10 6 L9 7 L8 6 H6 L5 7 Z M4.5 8 H9.5 V10.5 H4.5 Z" fill="#fff"/></svg>
        05550 111 333
      </p>
      <p class="contact-row">
        <svg viewBox="0 0 14 14"><circle cx="7" cy="7" r="7" fill="#ec1f27"/><rect x="3.5" y="4.5" width="7" height="5" fill="none" stroke="#fff" stroke-width="1"/><path d="M3.5 4.5 L7 7.3 L10.5 4.5" fill="none" stroke="#fff" stroke-width="1"/></svg>
        mdelaney@solvanta.com
      </p>
    </div>
    <div class="person">
      <p class="full-name">MARK DELANEY</p>
      <p class="role">DIRECTOR</p>
    </div>
    <div class="accent-bar"></div>
  </section>
</main>
</body>
</html>
```